Plum Petal Menstrual Cup Packaging and Leaflet

I have two sizes for menstrual cups for women; size 1 and size 2.
I need an Australian compliant packaging to fit the menstrual cup which is fun, flirty, cheeky and feminine, and a supporting leaflet with similar branding.
I've added the logo and some concepts for colours and themes for reference only.

Target Market(s)

Women 16-46 years of age

Industry/Entity Type

Feminine hygiene products

Font styles to use
Other font styles liked:
• Lobster, Cabin

Colors
EE7325
F08F49
F5BC92
FAE3D3
FDF4ED
EB3D1F
EC4F4E
F09395
F8D3D4
FCEDEE
E54698
E96AAD
F1A4CE
F9D9EA
FCEFF6

Requirements
Must have
• Reusable, recyclable packaging, Australian company, logo
Nice to have
• Unique style or shape

```html
<!DOCTYPE html>
<html lang="en">
<head>
<meta charset="utf-8">
<title>Plum Petal Menstrual Cup – Size 1 Carton</title>
<link rel="stylesheet" href="https://fonts.googleapis.com/css2?family=Cabin:wght@500;600;700&family=Outfit:wght@800&display=swap">
<style>
  :root {
    --backdrop: #cc2a58;
    --front-top: #e27c7a;
    --front-mid: #e69b6c;
    --front-bottom: #e2c222;
    --side-top: #fba6a1;
    --side-mid: #ffc88c;
    --side-bottom: #fde25a;
    --ink-light: #ffffff;
    --pill-bg: #f4efee;
    --pill-ink: #e5875f;
    --brand-ink: #fcedee;
    --product-light: #efd6da;
    --product-deep: #e54678;
  }
  * { margin: 0; padding: 0; box-sizing: border-box; }
  html, body {
    width: 1200px; height: 800px; overflow: hidden;
    background: var(--backdrop);
    font-family: "Cabin", sans-serif;
  }
  .carton {
    position: absolute; left: 380px; top: 80px;
    display: flex; height: 640px;
  }
  .side-panel {
    width: 130px; height: 100%;
    background: linear-gradient(180deg, var(--side-top) 0%, var(--side-mid) 50%, var(--side-bottom) 100%);
    position: relative;
  }
  .side-copy {
    position: absolute; left: 12px; right: 12px; top: 500px;
    color: var(--ink-light);
    font-size: 5.5px; line-height: 1.35; text-align: center;
  }
  .side-copy p + p { margin-top: 5px; }
  .front-panel {
    width: 310px; height: 100%;
    background: linear-gradient(180deg, var(--front-top) 0%, var(--front-mid) 50%, var(--front-bottom) 100%);
    position: relative;
    display: flex; flex-direction: column; align-items: center;
  }
  .brand-name {
    margin-top: 96px;
    font-family: "Cabin", sans-serif; font-weight: 700;
    font-size: 30px; color: var(--brand-ink);
  }
  .product-title {
    margin-top: 62px;
    font-family: "Outfit", sans-serif; font-weight: 800;
    font-size: 26px; letter-spacing: 0.5px;
    color: var(--ink-light);
  }
  .tagline-pill {
    margin-top: 6px;
    width: 234px; height: 20px; border-radius: 10px;
    background: var(--pill-bg); color: var(--pill-ink);
    font-weight: 600; font-size: 12.5px;
    display: flex; align-items: center; justify-content: center;
  }
  .product-visual {
    margin-top: 32px;
    width: 175px; height: 175px; border-radius: 50%;
    background: radial-gradient(circle at 50% 45%, var(--product-deep) 0%, #e86a90 28%, var(--product-light) 55%);
  }
  .product-blurb {
    margin-top: 68px;
    width: 220px; text-align: center;
    color: var(--ink-light); font-weight: 600;
    font-size: 9.5px; line-height: 1.12;
  }
  .size-label {
    margin-top: 22px;
    font-family: "Outfit", sans-serif; font-weight: 800;
    font-size: 26px; color: var(--ink-light);
  }
</style>
</head>
<body>
  <main class="carton">
    <section class="side-panel">
      <div class="side-copy">
        <p>Lorem ipsum dolor sit amet, consectetur adipiscing elit, sed do eiusmod tempor incididunt ut labore et dolore magna aliqua.</p>
        <p>Lorem ipsum dolor sit amet, consectetur adipiscing elit, sed do eiusmod tempor incididunt ut labore et dolore magna aliqua.</p>
      </div>
    </section>
    <section class="front-panel">
      <h1 class="brand-name">Plum Petal</h1>
      <h2 class="product-title">MENSTRUAL CUP</h2>
      <div class="tagline-pill">Lorem ipsum dolor sit amet</div>
      <div class="product-visual" role="img" aria-label="Product photo of a pink silicone menstrual cup"></div>
      <p class="product-blurb">Lorem ipsum dolor sit amet, consectetur adipiscing elit, sed do eiusmod tempor incididunt ut labore et dolore magna aliqua.</p>
      <p class="size-label">SIZE 1</p>
    </section>
  </main>
</body>
</html>
```